Website Design - Financial Services Software

We are looking for website designs for our public website.
Some competitor sites we like are
www.ledgerwick.com.au
www.pluvo.com.au
www.plannerbeam.com
www.quorvia.com.au

A wireframe example of our site can be found at
http://tmw4rp.draftpane.com/

Attached is our logo.

Industry/Entity Type

Financial

```html
<!DOCTYPE html>
<html lang="en">
<head>
<meta charset="utf-8">
<title>Valoris — Smarter Financial Strategies</title>
<link href="https://fonts.googleapis.com/css2?family=Libre+Baskerville:wght@400;700&family=Lato:wght@300;400;700&display=swap" rel="stylesheet">
<style>
:root{
  --gold:#cf9f45;
  --gold-light:#e2b565;
  --gold-deep:#b8872f;
  --brown:#6b4a14;
  --ink:#333;
  --muted:#8a93a3;
  --nav-bg:#f3f3f3;
  --footer:#434a54;
  --footer-deep:#2f3339;
  --cta:#f2b10c;
  --white:#fff;
}
*{margin:0;padding:0;box-sizing:border-box}
html,body{width:1024px;height:1200px;overflow:hidden}
body{position:relative;font-family:'Lato',sans-serif;color:var(--ink);background:var(--white)}
.abs{position:absolute}

.hero{left:0;top:0;width:1024px;height:414px;
  background:linear-gradient(115deg,#dcae5e 0%,#e3b86a 45%,#d3a453 60%,#c08b38 100%)}
.hero-sheen{left:0;top:0;width:1024px;height:414px;
  background:linear-gradient(105deg,transparent 62%,rgba(255,255,255,.12) 62%,rgba(255,255,255,.05) 100%)}
.navbar{left:0;top:36px;width:1024px;height:42px;background:linear-gradient(#fafafa,#ebebeb);border-bottom:1px solid #d8d8d8}
.nav-item{top:36px;height:42px;line-height:42px;font-family:'Libre Baskerville',serif;font-weight:700;font-size:11.5px;color:#7a5a22}
.nav-home{left:369px;width:57px;text-align:center;background:var(--gold);color:var(--white)}
.btn-small{top:43px;height:27px;line-height:26px;text-align:center;font-family:'Libre Baskerville',serif;font-weight:700;font-size:11.5px;color:var(--white);border-radius:2px}
.btn-login{left:746px;width:61px;background:linear-gradient(#b9b9b9,#9d9d9d)}
.btn-signup{left:814px;width:63px;background:linear-gradient(#d5a74e,#bd8a31);border:1px solid #a77a28}

.logo-box{left:138px;top:0;width:146px;height:113px;background:var(--white);border:1px solid #ddd;border-top:0;box-shadow:0 1px 3px rgba(0,0,0,.12);text-align:center}
.logo-mark{position:absolute;left:59px;top:20px;width:28px;height:28px;background:var(--gold)}
.logo-name{position:absolute;left:0;right:0;top:66px;font-family:'Libre Baskerville',serif;font-size:19px;color:var(--gold-deep);letter-spacing:1px}

.hero-title{left:138px;top:146px;font-family:'Libre Baskerville',serif;font-variant:small-caps;font-size:31px;line-height:36px;color:var(--white);text-shadow:0 1px 1px rgba(0,0,0,.15)}
.hero-sub{left:138px;top:225px;width:360px;font-size:19.5px;line-height:24px;color:var(--brown)}
.tour-card{top:291px;width:176px;height:67px;border-radius:3px;overflow:hidden}
.tour-photo{width:100%;height:100%}
.tour-label{position:absolute;left:0;right:0;bottom:0;height:30px;line-height:30px;text-align:center;color:var(--white);font-size:12.5px;background:linear-gradient(transparent,rgba(0,0,0,.45))}
.tour-link{top:367px;width:176px;text-align:center;font-family:'Libre Baskerville',serif;font-weight:700;font-size:9.5px;color:var(--white);text-decoration:underline}

.video{left:514px;top:150px;width:368px;height:208px;border-radius:3px;overflow:hidden}
.video-bar{left:0;bottom:0;width:100%;height:30px;background:rgba(25,25,25,.85)}
.vid-tag{top:8px;width:40px;height:42px;background:rgba(30,30,30,.85);border-radius:3px;color:#fff;font-size:8px;text-align:center;padding-top:28px}

.features{left:0;top:414px;width:1024px;height:380px;background:var(--white)}
.section-title{left:0;top:450px;width:1024px;text-align:center;font-family:'Libre Baskerville',serif;font-size:21px;color:var(--ink)}
.section-title span{color:var(--gold)}
.section-lede{left:330px;top:492px;width:364px;text-align:center;font-size:10.5px;line-height:16px;color:var(--muted)}
.feature-icon{width:43px;height:43px;background:var(--gold);display:flex;align-items:center;justify-content:center}
.feature-title{font-family:'Libre Baskerville',serif;font-size:14.5px;color:var(--ink)}
.feature-text{width:188px;font-size:10.5px;line-height:16px;color:var(--muted)}

.cta{left:0;top:794px;width:1024px;height:166px;background:linear-gradient(100deg,#c8963f 0%,#dcad5f 45%,#c99645 75%,#a87624 100%)}
.cta-title{left:0;top:833px;width:1024px;text-align:center;font-family:'Libre Baskerville',serif;font-size:21px;color:var(--white)}
.cta-sub{left:0;top:864px;width:1024px;text-align:center;font-size:12px;font-weight:300;color:#fbeed4}
.cta-btn{left:439px;top:896px;width:120px;height:32px;line-height:31px;text-align:center;background:linear-gradient(#f7bf1d,#eda806);border:1px solid #d99800;color:var(--white);font-size:11.5px}

.footer{left:0;top:960px;width:1024px;height:196px;background:var(--footer)}
.footer-logo{left:138px;top:1003px;width:137px;height:110px;text-align:center}
.footer-mark{position:absolute;left:51px;top:8px;width:34px;height:34px;background:var(--white)}
.footer-name{position:absolute;left:0;right:0;top:76px;font-family:'Libre Baskerville',serif;font-size:22px;color:var(--white);letter-spacing:1px}
.col-head{top:1000px;font-size:11px;font-weight:700;color:#a9afba}
.col-link{font-size:10.5px;color:var(--white)}
.social-box{width:21px;height:21px;background:var(--white);border-radius:2px}
.legal-bar{left:0;top:1156px;width:1024px;height:44px;background:var(--footer-deep)}
.copyright{left:138px;top:1172px;font-size:10.5px;color:#7f8692}
</style>
</head>
<body>

<div class="abs hero"></div>
<div class="abs hero-sheen"></div>
<div class="abs navbar"></div>
<div class="abs nav-item nav-home">Home</div>
<div class="abs nav-item" style="left:454px">Features</div>
<div class="abs nav-item" style="left:533px">Examples</div>
<div class="abs nav-item" style="left:621px">FAQ</div>
<div class="abs nav-item" style="left:687px">About</div>
<div class="abs btn-small btn-login">Login</div>
<div class="abs btn-small btn-signup">Sign Up</div>

<div class="abs logo-box">
  <div class="logo-mark"></div>
  <div class="logo-name">VALORIS</div>
</div>

<div class="abs hero-title">Smarter Financial<br>Strategies</div>
<div class="abs hero-sub">Values and Cash-flow focused financial software for financial planners.</div>

<div class="abs tour-card" style="left:136px">
  <div class="tour-photo" role="img" aria-label="Photo of a businessman in glasses on the phone" style="background:linear-gradient(120deg,#5c6a70,#9aa3a6 50%,#3c454a)"></div>
  <div class="tour-label">For Planning Practices</div>
</div>
<div class="abs tour-link" style="left:136px">TAKE TOUR</div>
<div class="abs tour-card" style="left:320px">
  <div class="tour-photo" role="img" aria-label="Photo of a group of business people in discussion" style="background:linear-gradient(120deg,#6f6760,#b0a69a 50%,#4a433d)"></div>
  <div class="tour-label">For Dealer Groups</div>
</div>
<div class="abs tour-link" style="left:320px">TAKE TOUR</div>

<div class="abs video">
  <div class="abs" role="img" aria-label="Video still of city office towers under a blue sky" style="left:0;top:0;width:100%;height:100%;background:linear-gradient(180deg,#b9c7d6 0%,#8ea7c3 45%,#6f7f88 72%,#354030 100%)"></div>
  <div class="abs vid-tag" style="left:18px">Share</div>
  <div class="abs vid-tag" style="left:62px">Playlist</div>
  <div class="abs vid-tag" style="left:106px">Love</div>
  <svg class="abs" style="left:28px;top:14px" width="110" height="18" fill="none" stroke="#fff" stroke-width="1.3">
    <rect x="4" y="3" width="14" height="11" rx="2"/>
    <ellipse cx="54" cy="5" rx="6" ry="2.5"/><path d="M48 5v8c0 1.4 2.7 2.5 6 2.5s6-1.1 6-2.5V5"/>
    <path d="M101 15l-6-6a3.5 3.5 0 015-5l1 1 1-1a3.5 3.5 0 015 5z"/>
  </svg>
  <div class="abs video-bar">
    <svg class="abs" style="left:0;top:0" width="368" height="30">
      <circle cx="19" cy="15" r="6.5" fill="none" stroke="#fff" stroke-width="1.5"/>
      <path d="M17 12l5 3-5 3z" fill="#fff"/>
      <path d="M38 12h3l4-3v12l-4-3h-3z" fill="#e2ad3c"/>
      <g fill="#e2ad3c"><rect x="55" y="11" width="1.5" height="8"/><rect x="59" y="11" width="1.5" height="8"/><rect x="63" y="11" width="1.5" height="8"/><rect x="67" y="11" width="1.5" height="8"/><rect x="71" y="11" width="1.5" height="8"/></g>
      <g fill="#777"><rect x="75" y="11" width="1.5" height="8"/><rect x="79" y="11" width="1.5" height="8"/></g>
      <rect x="93" y="14" width="160" height="2.5" fill="#666"/>
      <rect x="93" y="14" width="57" height="2.5" fill="#e2ad3c"/>
      <text x="265" y="18" fill="#fff" font-size="8" font-family="Lato,sans-serif">01:30 / 04:55</text>
      <rect x="326" y="11" width="9" height="8" fill="none" stroke="#fff" stroke-width="1.5"/>
      <circle cx="351" cy="15" r="2.5" fill="none" stroke="#fff" stroke-width="1.5"/>
      <circle cx="351" cy="15" r="4.8" fill="none" stroke="#fff" stroke-width="1.5" stroke-dasharray="2 1.5"/>
    </svg>
  </div>
</div>

<div class="abs features"></div>
<div class="abs section-title">Core Features of <span>Valoris</span></div>
<div class="abs section-lede">Maecenas bibendum lacus gravida placerat consequat. Vivamus quis hendrerit mauris. Vestibulum laoreet felis sed consectetur sollicitudin.</div>

<div class="abs feature-icon" style="left:126px;top:570px"><svg width="16" height="14" fill="#fff"><path d="M2 12C2 5 7 2 15 2c0 7-4 10-10 9l-3 2zM4 10c3-3 5-4 8-5-3 0-6 2-8 5z"/></svg></div>
<div class="abs feature-title" style="left:181px;top:563px">Feature Title</div>
<div class="abs feature-text" style="left:181px;top:586px">Nunc purus orci, adipiscing non ipsum non, pellentesque fringilla sapien. Phasellus lacus tellus, facilisis.</div>

<div class="abs feature-icon" style="left:395px;top:570px"><svg width="16" height="14" fill="#fff"><rect x="0" y="1" width="16" height="10" rx="1"/><rect x="2" y="3" width="12" height="6" fill="#cf9f45"/><rect x="6" y="11" width="4" height="2"/><rect x="4" y="13" width="8" height="1"/></svg></div>
<div class="abs feature-title" style="left:450px;top:563px">Feature Title</div>
<div class="abs feature-text" style="left:450px;top:586px">Nunc purus orci, adipiscing non ipsum non, pellentesque fringilla sapien. Phasellus lacus tellus, facilisis.</div>

<div class="abs feature-icon" style="left:664px;top:570px"><svg width="16" height="14" fill="#fff"><path d="M5 2h6l1 2h3v9H1V4h3z"/><circle cx="8" cy="8" r="3" fill="#cf9f45"/><circle cx="8" cy="8" r="1.7"/></svg></div>
<div class="abs feature-title" style="left:719px;top:563px">Feature Title</div>
<div class="abs feature-text" style="left:719px;top:586px">Nunc purus orci, adipiscing non ipsum non, pellentesque fringilla sapien. Phasellus lacus tellus, facilisis.</div>

<div class="abs feature-icon" style="left:126px;top:680px"><svg width="14" height="16" fill="#fff"><path d="M1 1h1v5h1V1h1v5h1V1h1v6l-1.5 1V15H3V8L1 7z"/><path d="M10 1c2 0 3 2 3 5v3h-1.5v6H9V1z"/></svg></div>
<div class="abs feature-title" style="left:181px;top:673px">Feature Title</div>
<div class="abs feature-text" style="left:181px;top:696px">Nunc purus orci, adipiscing non ipsum non, pellentesque fringilla sapien. Phasellus lacus tellus, facilisis.</div>

<div class="abs feature-icon" style="left:395px;top:680px"><svg width="16" height="16" fill="#fff"><path d="M6 1l5 5-3 3-5-5z"/><path d="M8 8l7 6-1.5 1.5L7 9z"/></svg></div>
<div class="abs feature-title" style="left:450px;top:673px">Feature Title</div>
<div class="abs feature-text" style="left:450px;top:696px">Nunc purus orci, adipiscing non ipsum non, pellentesque fringilla sapien. Phasellus lacus tellus, facilisis.</div>

<div class="abs feature-icon" style="left:664px;top:680px"><svg width="16" height="14" fill="#fff"><path d="M2 12C2 5 7 2 15 2c0 7-4 10-10 9l-3 2zM4 10c3-3 5-4 8-5-3 0-6 2-8 5z"/></svg></div>
<div class="abs feature-title" style="left:719px;top:673px">Feature Title</div>
<div class="abs feature-text" style="left:719px;top:696px">Nunc purus orci, adipiscing non ipsum non, pellentesque fringilla sapien. Phasellus lacus tellus, facilisis.</div>

<div class="abs cta"></div>
<div class="abs cta-title">Create an account today and begin your 30-day <b>FREE</b> trial!</div>
<div class="abs cta-sub">Nunc purus orci, adipiscing non ipsum non, pellentesque fringilla sapien.</div>
<div class="abs cta-btn">SIGN UP NOW</div>

<div class="abs footer"></div>
<div class="abs footer-logo">
  <div class="footer-mark"></div>
  <div class="footer-name">VALORIS</div>
</div>

<div class="abs col-head" style="left:375px">ABOUT</div>
<div class="abs col-link" style="left:375px;top:1041px">About Us</div>
<div class="abs col-link" style="left:375px;top:1075px">Support</div>

<div class="abs col-head" style="left:505px">GETTING STARTED</div>
<div class="abs col-link" style="left:505px;top:1041px">Why Valoris</div>
<div class="abs col-link" style="left:505px;top:1075px">Download a Summary</div>
<div class="abs col-link" style="left:505px;top:1110px">Valoris Videos</div>

<div class="abs col-head" style="left:632px">LEGAL</div>
<div class="abs col-link" style="left:632px;top:1041px">Terms of Use</div>
<div class="abs col-link" style="left:632px;top:1075px">Privacy</div>

<div class="abs col-head" style="left:761px">CONNECT</div>
<div class="abs social-box" style="left:761px;top:1039px"></div>
<div class="abs col-link" style="left:791px;top:1041px">Valoris on Linkwork</div>
<div class="abs social-box" style="left:761px;top:1072px"></div>
<div class="abs col-link" style="left:791px;top:1075px">Valoris on Chirper</div>

<div class="abs legal-bar"></div>
<div class="abs copyright">Copyright © 2014 - Valoris Pty Ltd. All Rights Reserved.</div>

</body>
</html>
```